Business Card Design - Furniture Retail

Open to both Single or double sided design

We are launching a online ecommerce store that sells Scandinavian/Danish style of furniture in Australia.

We aspire to provide stylish but classic and designers' selection of furniture to the Australia public at affordable price. For the style of the furniture we are selling, please see the following links:

https://www.filecrate.example/sh/qk3mzr8wlp/BXTpLnR4vQ7cYdHs?dl=0

The style of the design we are looking for is clean, simple that look Scandinavian/Danish but yet it is timeless classic.

Aspiring Design
http://www.lindmora.com
http://tobyquell.com.au/
http://vekt.furniture/
http://www.olvo.com/
Updates

Please display the card on normal angle for both front and back instead of funny angle. Please keep it display when displaying the design of the business cards so that we can focus on the designs rather than being confused by the unnecessary stuffs like the hands or background

I think there is already enough curve line on the logo itself so anything extra of the curve on the business card would be really unnecessary. Please avoid using any of the extra curve line on the business card, other than the logo itself. Thanks

Regular card and give them a matt celloglaze to create texture on card that makes it looked luxury and expensive.

Please display design on normal angle! Please only use white colour in the background (not the business card but the referring to the submission) rather than anything fancy so that we can focus on the design.

Target Market(s)

High end market consumers who are financially capable and who has good taste and appreciate good design

aged between 28 - 45 white collars professional/businessmen who live in metropolitan areas

Industry/Entity Type

Business

Font styles to use
Serif
Sans Serif

Requirements
Must have
• Regular card and give them a matt celloglaze to create texture on card that makes it looked luxury and expensive.

Please use the logo from the uploaded files

Company Name: Milo Verhagen
Name: Milo Reeb
Phone: +614 27 305 641
Website: www.miloverhagen.com.au
Email: milo@miloverhagen.com.au
Nice to have
• Colour is not limited to black and white
Should not have
• The concept photos of the furniture should NOT be used in the FRONT page of the business card.

```html
<!DOCTYPE html>
<html lang="en">
<head>
<meta charset="utf-8">
<title>Milo Verhagen — Business Card</title>
<link href="https://fonts.googleapis.com/css2?family=Jost:wght@400&display=swap" rel="stylesheet">
<style>
  :root {
    --page: #ffffff;
    --card-light: #ffffff;
    --card-dark: #2e343a;
    --ink-dark: #2e343a;
    --ink-light: #eef0f1;
    --ink-soft: #d6dadd;
    --edge: #e2e4e6;
  }
  * { margin: 0; padding: 0; box-sizing: border-box; }
  html, body {
    width: 1200px;
    height: 900px;
    overflow: hidden;
    background: var(--page);
    font-family: "Jost", "Futura", sans-serif;
  }
  .canvas {
    position: relative;
    width: 1200px;
    height: 900px;
  }
  .card {
    position: absolute;
    top: 302px;
    width: 514px;
    height: 295px;
    box-shadow: 0 2px 10px rgba(0, 0, 0, 0.12);
  }
  .card--front {
    left: 72px;
    background: var(--card-light);
    border: 1px solid var(--edge);
    display: flex;
    align-items: center;
    justify-content: center;
  }
  .card--back {
    left: 616px;
    background: var(--card-dark);
  }
  .wordmark {
    font-weight: 400;
    text-transform: uppercase;
    letter-spacing: 0.06em;
    white-space: nowrap;
    line-height: 1;
  }
  .card--front .wordmark {
    color: var(--ink-dark);
    font-size: 40px;
  }
  .contact {
    position: absolute;
    left: 48px;
    top: 40px;
    color: var(--ink-soft);
  }
  .contact__name {
    font-size: 16.5px;
    color: var(--ink-light);
    margin-bottom: 4px;
  }
  .contact__line {
    font-size: 11px;
    line-height: 18px;
    letter-spacing: 0.02em;
  }
  .brand-block {
    position: absolute;
    right: 48px;
    top: 200px;
    text-align: right;
  }
  .card--back .wordmark {
    color: var(--ink-light);
    font-size: 37px;
  }
  .tagline {
    margin-top: 8px;
    font-size: 12.5px;
    color: var(--ink-soft);
    letter-spacing: 0.01em;
  }
</style>
</head>
<body>
<main class="canvas">
  <section class="card card--front" aria-label="Card front">
    <div class="wordmark">Milo Verhagen</div>
  </section>

  <section class="card card--back" aria-label="Card back">
    <div class="contact">
      <p class="contact__name">Milo Reeb</p>
      <p class="contact__line">+614 27 305 641</p>
      <p class="contact__line">milo@miloverhagen.com.au</p>
      <p class="contact__line">www.miloverhagen.com.au</p>
    </div>
    <div class="brand-block">
      <div class="wordmark">Milo Verhagen</div>
      <p class="tagline">Scandinavian style of furniture</p>
    </div>
  </section>
</main>
</body>
</html>
```